CREATE A KILLER WEBSITE DESIGN

We are a firearms training company that trains CIVILIANS (no police or military pictures - thank you!) to defend themselves and are looking for a killer design that's clean, easy to navigate and modern! We want the newest trends applied to this sight like a scrollable site so you can scroll down and see all the features. We are okay with tweaking the HTML but need the artistic design to look good. I'll provide a link to our current site along with a sight we really like so you can get an idea!

I'm supplying a PowerPoint Design we are going with from another designer so you can match the style to the new site.

PAGES: (Please use information from our current site. We like the information but just want a more polished look similar to the NWDFA site below but in our colors.)
Home - Long Form Scrolling Site. Top fold will be a video with a play button.
Falconry Institute - Seven Level Training Program Info Page That Will Contain A Video.
Contact Us - This will be a page that DOES NOT CONTAIN AN EMAIL ADDRESS. Just a contact us form
Meet The Trainer: Brendan Osterlow

Our site:
https://www.brightharborguarding.biz

Sights We Like:
https://www.nwdefenderalliance.com
https://quorvel.com
https://brinmoreworkscorp.com
https://www.pelldrivegear.com

Target Market(s)

Men and women ages 21 to 100 years old

Industry/Entity Type

Self Defense

Number of Pages Required

5+ page

Font styles to use
Sans Serif

Colors
f26267

Requirements
Must have
• Clean and engaging. Use of colors that match our logo.
Should not have
• Poor design quality

```html
<!DOCTYPE html>
<html lang="en">
<head>
<meta charset="utf-8">
<title>Bright Harbor Guarding</title>
<link href="https://fonts.googleapis.com/css2?family=Audiowide&family=Barlow+Condensed:ital,wght@0,500;0,600;1,400;1,500;1,600&display=swap" rel="stylesheet">
<style>
:root{
  --red:#e31b1b;
  --ink:#1d1d1f;
  --dark:#232224;
  --grey:#ececec;
  --mid:#8a8a8a;
  --white:#ffffff;
  --head:'Audiowide',sans-serif;
  --body:'Barlow Condensed',sans-serif;
}
*{margin:0;padding:0;box-sizing:border-box}
html,body{width:1200px;height:3497px;overflow:hidden}
body{position:relative;background:var(--white);font-family:var(--body);color:var(--ink)}
.abs{position:absolute}
.italic{font-style:italic}
.head{font-family:var(--head);text-transform:uppercase}
.red{color:var(--red)}

/* header */
.site-header{position:absolute;left:0;top:0;width:1200px;height:125px;background:var(--white)}
.brand{position:absolute;left:0;top:0;width:360px;height:170px;background:var(--white);clip-path:polygon(0 0,100% 0,92% 100%,0 100%);z-index:3;display:flex;flex-direction:column;align-items:center;justify-content:center;padding-left:10px}
.brand-mark{width:70px;height:70px;border-radius:50%;background:var(--red);margin-bottom:8px}
.brand-name{font-family:var(--head);color:var(--red);font-size:19px;text-align:center;line-height:1.1;width:240px}
.notice{left:439px;top:10px;width:450px;font-size:10.5px;line-height:1.25;color:#333}
.urgent{left:897px;top:14px;font-size:14px;font-style:italic;font-weight:600;display:flex;align-items:center;gap:6px}
.info-bar{position:absolute;left:292px;top:47px;width:908px;height:34px;background:var(--red);clip-path:polygon(0 0,100% 0,100% 100%,28px 100%)}
.info-bar .dark{position:absolute;left:150px;top:0;width:48px;height:34px;background:var(--ink);clip-path:polygon(20px 0,100% 0,28px 100%,0 100%)}
.info-item{position:absolute;top:8px;color:var(--white);font-size:14px;font-style:italic;font-weight:600;display:flex;align-items:center;gap:10px}
.main-nav{position:absolute;left:439px;top:94px;display:flex;align-items:center;gap:14px;font-family:var(--head);font-size:14.5px;text-transform:uppercase}
.dot{width:12px;height:12px;border-radius:50%;border:2px solid var(--red);position:relative}
.dot::after{content:"";position:absolute;left:2px;top:2px;width:4px;height:4px;border-radius:50%;background:var(--red)}

/* hero */
.hero{position:absolute;left:0;top:125px;width:1200px;height:459px;background:linear-gradient(100deg,#c9a58e 0%,#8e6f61 30%,#6e5650 50%,#4a3b3c 70%,#5d3131 100%)}
.hero-title{left:740px;top:112px;font-family:var(--head);font-size:35px;line-height:0.87;text-transform:uppercase;color:var(--white)}
.hero-copy{left:739px;top:244px;width:290px;color:var(--white);font-size:15px;font-style:italic;line-height:1.05}
.btn{display:inline-flex;align-items:center;justify-content:center;gap:6px;background:var(--red);color:var(--white);font-style:italic;font-weight:600;font-size:13.5px;text-transform:uppercase;clip-path:polygon(10px 0,100% 0,calc(100% - 10px) 100%,0 100%)}
.hero .btn{position:absolute;left:746px;top:320px;width:165px;height:34px}
.hero .ghost{position:absolute;left:933px;top:328px;color:var(--white);font-style:italic;font-weight:600;font-size:13.5px;text-transform:uppercase}
.slider-dots{display:flex;gap:4px}
.slider-dots i{display:block;width:14px;height:2px;background:#bbb}
.slider-dots i.on{background:var(--red)}

/* press */
.press{position:absolute;left:0;top:584px;width:1200px;height:190px;background:var(--grey)}
.press-card{position:absolute;top:39px;width:205px;height:115px;background:var(--white);box-shadow:0 3px 12px rgba(0,0,0,.12);display:flex;align-items:center;justify-content:center;font-family:var(--head);font-size:20px;color:var(--ink);text-align:center;line-height:1}

/* about */
.section-title{font-family:var(--head);text-transform:uppercase;font-size:35px;line-height:1.1}
.about-text{left:145px;top:952px;width:455px;font-size:13px;font-style:italic;line-height:1.25;color:#333}
.about-text p+p{margin-top:13px}
.rule{position:absolute;left:145px;top:1290px;width:910px;height:1px;background:#ddd}

/* levels */
.center{left:0;width:1200px;text-align:center}
.intro{top:1496px;font-size:17px;font-style:italic;line-height:1.3;color:#333}
.levels-text{left:601px;top:1594px;width:452px;font-size:13.5px;font-style:italic;line-height:1.2;color:#333}
.level{position:absolute;display:flex;gap:8px}
.level .num{font-family:var(--head);font-size:40px;color:#e2e2e2;line-height:0.9}
.level .name{font-family:var(--head);font-size:14px;text-transform:uppercase;line-height:1.15;padding-top:4px}
.level .name::after{content:"";display:block;width:18px;height:3px;background:var(--red);margin-top:8px}

/* video */
.video{position:absolute;left:0;top:2036px;width:1200px;height:400px;background:linear-gradient(90deg,#3b3a3e 0%,#6c6765 40%,#a89b8c 70%,#d4c2aa 100%)}
.play{position:absolute;left:550px;top:180px;width:96px;height:64px;border-radius:12px;background:rgba(255,255,255,.85)}

/* stories */
.stories{position:absolute;left:0;top:2436px;width:1200px;height:523px;background:var(--grey)}
.story{position:absolute;top:189px;width:277px;height:242px;background:var(--white);box-shadow:0 3px 12px rgba(0,0,0,.1);padding:30px 32px}
.quote{font-family:Georgia,serif;font-size:70px;line-height:0.7;color:var(--red);font-weight:700;height:40px}
.story p{font-size:14.5px;font-style:italic;line-height:1.3;color:#333;height:112px}
.story .who{font-family:var(--head);font-size:13.5px;text-transform:uppercase}
.story .when{font-family:var(--head);font-size:11px;color:var(--red)}
.story .when::after{content:"";display:block;width:18px;height:3px;background:var(--red);margin-top:14px}

/* footer */
.site-footer{position:absolute;left:0;top:2959px;width:1200px;height:538px;background:var(--dark);color:var(--white)}
.footer-bar{position:absolute;left:271px;top:65px;width:929px;height:34px;background:var(--red);clip-path:polygon(0 0,100% 0,100% 100%,28px 100%)}
.footer-brand{left:145px;top:72px;width:180px;text-align:center}
.footer-brand .mark{width:52px;height:52px;border-radius:50%;background:var(--white);margin:0 auto 8px}
.footer-brand .nm{font-family:var(--head);font-size:19px;line-height:1.05}
.field{position:absolute;width:257px;height:43px;border:1px solid #6a6a6c;font-size:12px;font-style:italic;padding:14px 16px;color:#ddd}
.site-footer .btn{position:absolute;left:532px;top:307px;width:167px;height:32px}
.footer-nav{position:absolute;left:145px;top:420px;display:flex;align-items:center;gap:16px;font-family:var(--head);font-size:14.5px;text-transform:uppercase}
.social{position:absolute;left:955px;top:423px;display:flex;gap:20px;font-size:13px;font-weight:600}
.copyright{position:absolute;left:0;top:497px;width:1200px;text-align:center;font-size:12px;font-style:italic;color:#bbb}
.footer-rule{position:absolute;left:145px;top:461px;width:910px;height:1px;background:#3a393b}
</style>
</head>
<body>

<header class="site-header">
  <div class="brand">
    <div class="brand-mark"></div>
    <div class="brand-name">BRIGHT HARBOR GUARDING</div>
  </div>
  <p class="abs notice">Due to an increase in demand, we may not be able to answer your call, text or email immediately. Please be patient and know that we value your business and will respond to you as quickly as we can.</p>
  <div class="abs urgent">
    <svg width="16" height="14" viewBox="0 0 16 14"><path d="M1 6 15 1 10 13 8 8Z" fill="none" stroke="#e31b1b" stroke-width="1.4"/></svg>
    I NEED IMMEDIATE SERVICE
  </div>
  <div class="info-bar">
    <div class="dark"></div>
    <div class="info-item" style="left:168px">
      <svg width="18" height="18" viewBox="0 0 24 24"><path d="M6.6 10.8a15 15 0 0 0 6.6 6.6l2.2-2.2c.3-.3.7-.4 1-.2 1.1.4 2.3.6 3.6.6.6 0 1 .4 1 1V20c0 .6-.4 1-1 1A17 17 0 0 1 3 4c0-.6.4-1 1-1h3.5c.6 0 1 .4 1 1 0 1.3.2 2.5.6 3.6.1.3 0 .7-.2 1z" fill="#fff"/></svg>
      555-014-BHG (0244)
    </div>
    <div class="info-item" style="left:365px">
      <svg width="14" height="18" viewBox="0 0 14 18"><path d="M7 0a7 7 0 0 0-7 7c0 5 7 11 7 11s7-6 7-11a7 7 0 0 0-7-7zm0 9.5A2.5 2.5 0 1 1 7 4.5a2.5 2.5 0 0 1 0 5z" fill="#fff"/></svg>
      P.O. BOX 4410 CEDAR POINT, FL 32000
    </div>
    <div class="info-item" style="left:702px">
      LOG IN
      <svg width="20" height="18" viewBox="0 0 20 18"><path d="M9 1h10v16H9M1 9h12M9 5l4 4-4 4" fill="none" stroke="#fff" stroke-width="1.6"/></svg>
    </div>
  </div>
  <nav class="main-nav">
    <span>Home</span><span class="dot"></span>
    <span>Falconry Institute</span><span class="dot"></span>
    <span>Contact Us</span><span class="dot"></span>
    <span>Meet The Trainer</span>
  </nav>
</header>

<section class="hero" role="img" aria-label="Photo of a civilian in ear protection aiming a scoped rifle at an indoor range">
  <h1 class="abs hero-title">Firearms<br>Training<br><span class="red">With Certified<br>Trainers</span></h1>
  <p class="abs hero-copy">Your life may depend on what you learn in your concealed carry training - don't settle for a gun shop class!</p>
  <span class="btn">Get Tickets Now
    <svg width="7" height="11" viewBox="0 0 7 11"><path d="M1 1l4.5 4.5L1 10" fill="none" stroke="#fff" stroke-width="1.6"/></svg></span>
  <span class="ghost">Falconry Institute &gt;</span>
  <div class="abs slider-dots" style="left:571px;top:416px"><i></i><i class="on"></i><i></i></div>
</section>

<section class="press">
  <div class="press-card" style="left:145px">HARLOW<br>REPORT</div>
  <div class="press-card" style="left:380px">MERIDIAN<br>NEWSLINE</div>
  <div class="press-card" style="left:615px">COASTAL SEVEN</div>
  <div class="press-card" style="left:850px">BRIGHTLINE</div>
</section>

<section class="about">
  <div class="abs" style="left:145px;top:858px;display:flex;gap:8px;align-items:flex-start">
    <svg width="34" height="34" viewBox="0 0 34 34" style="margin-top:4px"><circle cx="17" cy="17" r="15" fill="none" stroke="#e31b1b" stroke-width="2.5"/><circle cx="17" cy="17" r="9" fill="none" stroke="#e31b1b" stroke-width="2.5"/><circle cx="17" cy="17" r="4" fill="#e31b1b"/></svg>
    <h2 class="section-title">About The Instructor<br><span class="red">Brendan Osterlow</span></h2>
  </div>
  <div class="abs about-text">
    <p>Brendan Osterlow is a 3rd generation Cedar Point native and delighted to be a part of this great community. He is a true security expert with 25 years of experience in the security industry. He has appeared on Harlow Report, Coastal Seven, Brightline &amp; Meridian news outlets. He has been Featured in numerous publications and has trained thousands to protect themselves and their homes from thugs and thieves. He is certified by both the NMSA &amp; the NWDFA as a firearms instructor. He is also an NMSA Range Safety Officer and Defensive Pistol Instructor. He often says: "My students are like family so I take their security personal. I want them to feel confident that they can protect themselves and their families!"</p>
    <p>Bright Harbor Guarding is a radically different concealed carry class focusing on the TRUTH about how "Real Attacks" take place. The Concealed Carry Class goes over way more than just the boring, lecture-style, gun shop curriculum into real strategies, tactics and training suggestions to help you prepare! You have to experience it to believe it! We also offer The Falconry Institute for those who are looking for a Fully Immersive, Reality Based training environment that prepares you to defend against the worst threats you may face! In The Institute, we utilize high tech, military/law enforcement grade simulators to take training to a level never before seen in the world of concealed carry.</p>
  </div>
  <svg class="abs" style="left:631px;top:848px" width="414" height="357" viewBox="0 0 414 357">
    <polygon points="207,0 414,357 0,357" fill="#e31b1b"/>
    <polygon points="207,22 385,340 29,340" fill="#fff"/>
    <polygon points="207,40 360,318 54,318" fill="#3a3a3a" role="img" aria-label="Black and white portrait of the instructor"/>
  </svg>
  <div class="rule"></div>
</section>

<section class="levels">
  <svg class="abs" style="left:584px;top:1351px" width="32" height="32" viewBox="0 0 34 34"><circle cx="17" cy="17" r="15" fill="none" stroke="#e31b1b" stroke-width="2.5"/><circle cx="17" cy="17" r="9" fill="none" stroke="#e31b1b" stroke-width="2.5"/><circle cx="17" cy="17" r="4" fill="#e31b1b"/></svg>
  <h2 class="abs center section-title" style="top:1394px">Our 7 Levels Of Training Take You<br><span class="red">From Zero To Hero</span></h2>
  <p class="abs center intro">Wanna hear something funny? Guess what the average person asks about a concealed weapons class?<br>"How much is it and how long is it?" Can you believe it? We are talking about preparing you for life and death<br>situations and the main concern is "How Fast" and "How Cheap?" WOW!</p>
  <svg class="abs" style="left:145px;top:1588px" width="412" height="360" viewBox="0 0 412 360">
    <polygon points="206,0 412,360 0,360" fill="#e31b1b"/>
    <polygon points="206,30 388,340 24,340" fill="#fff"/>
    <rect x="36" y="30" width="340" height="300" fill="#8a8f72" role="img" aria-label="Photo of a man and a woman in safety glasses aiming handguns outdoors"/>
  </svg>
  <p class="abs levels-text">Why do most people settle for a cheap &amp; quick concealed carry class? It's a fair question! Could you imagine a military soldier trained by a 2-hour class? How effective would they be in the heat of battle? If you want to be ready to SURVIVE an attack, YOU NEED MORE than a basic, run of the mill class! That's why we created a <b>PROPRIETARY 7 LEVEL TRAINING SYSTEM</b> to take you all the way to the peak of readiness!</p>
  <div class="level" style="left:601px;top:1716px"><span class="num">1</span><span class="name">Concealed<br>Carry Class</span></div>
  <div class="level" style="left:770px;top:1716px"><span class="num">2</span><span class="name">Dynamic<br>Defensive<br>Shooting</span></div>
  <div class="level" style="left:922px;top:1716px"><span class="num">3</span><span class="name">Fine Tuning<br>Your<br>Technique</span></div>
  <div class="level" style="left:601px;top:1807px"><span class="num">4</span><span class="name">Virtual<br>Threat-Lab</span></div>
  <div class="level" style="left:770px;top:1807px"><span class="num">5</span><span class="name">Tactical<br>Skills &amp;<br>Drills</span></div>
  <div class="level" style="left:922px;top:1807px"><span class="num">6</span><span class="name">Close<br>Quarters<br>Defense</span></div>
  <div class="level" style="left:601px;top:1900px"><span class="num">7</span><span class="name">Live Scenario<br>Threat-Lab</span></div>
  <span class="btn abs" style="left:889px;top:1907px;width:166px;height:34px">Get Tickets Now &gt;</span>
</section>

<section class="video" role="img" aria-label="Video still of civilians in ear and eye protection firing handguns at an outdoor range">
  <div class="play">
    <svg width="96" height="64" viewBox="0 0 96 64"><polygon points="38,18 62,32 38,46" fill="#333"/></svg>
  </div>
</section>

<section class="stories">
  <svg class="abs" style="left:584px;top:63px" width="32" height="32" viewBox="0 0 34 34"><circle cx="17" cy="17" r="15" fill="none" stroke="#e31b1b" stroke-width="2.5"/><circle cx="17" cy="17" r="9" fill="none" stroke="#e31b1b" stroke-width="2.5"/><circle cx="17" cy="17" r="4" fill="#e31b1b"/></svg>
  <h2 class="abs center section-title" style="top:106px">Success Stories</h2>
  <article class="story" style="left:145px">
    <div class="quote">&ldquo;</div>
    <p>I had never held a gun when I took the Bright Harbor Guarding class and I'm hooked! I'm going all the way to level 7! Thank you Bright Harbor Guarding!</p>
    <div class="who">Corinne P.</div><div class="when">October 14, 2017</div>
  </article>
  <article class="story" style="left:461px">
    <div class="quote">&ldquo;</div>
    <p>I was mugged here in Cedar Point and lived in fear ever since. It stole my happiness and I became scared to go out. I'm a Level 4 student and I feel sorry for the next thug that tries me!</p>
    <div class="who">Delia R.</div><div class="when">December 9, 2017</div>
  </article>
  <article class="story" style="left:776px">
    <div class="quote">&ldquo;</div>
    <p>I've been shooting for years and already had my concealed weapons license. My first class was a gun shop class and a waste of money. Brendan took the time to show ...</p>
    <div class="who">Marcus T.</div><div class="when">March 3 2018</div>
  </article>
  <div class="abs slider-dots" style="left:571px;top:480px"><i class="on"></i><i class="on"></i><i class="on"></i></div>
</section>

<footer class="site-footer">
  <div class="footer-bar">
    <div class="info-item" style="left:168px">
      <svg width="18" height="18" viewBox="0 0 24 24"><path d="M6.6 10.8a15 15 0 0 0 6.6 6.6l2.2-2.2c.3-.3.7-.4 1-.2 1.1.4 2.3.6 3.6.6.6 0 1 .4 1 1V20c0 .6-.4 1-1 1A17 17 0 0 1 3 4c0-.6.4-1 1-1h3.5c.6 0 1 .4 1 1 0 1.3.2 2.5.6 3.6.1.3 0 .7-.2 1z" fill="#fff"/></svg>
      555-014-BHG (0244)
    </div>
    <div class="info-item" style="left:386px">
      <svg width="14" height="18" viewBox="0 0 14 18"><path d="M7 0a7 7 0 0 0-7 7c0 5 7 11 7 11s7-6 7-11a7 7 0 0 0-7-7zm0 9.5A2.5 2.5 0 1 1 7 4.5a2.5 2.5 0 0 1 0 5z" fill="#fff"/></svg>
      P.O. BOX 4410 CEDAR POINT, FL 32000
    </div>
    <div class="info-item" style="left:723px">LOG IN
      <svg width="20" height="18" viewBox="0 0 20 18"><path d="M9 1h10v16H9M1 9h12M9 5l4 4-4 4" fill="none" stroke="#fff" stroke-width="1.6"/></svg>
    </div>
  </div>
  <div class="abs footer-brand">
    <div class="mark"></div>
    <div class="nm">FALCONRY INSTITUTE</div>
  </div>
  <div class="abs head" style="left:145px;top:230px;font-size:14.5px">Brendan Osterlow</div>
  <div class="abs" style="left:145px;top:255px;width:18px;height:3px;background:var(--red)"></div>
  <p class="abs italic" style="left:145px;top:277px;width:270px;font-size:13px;line-height:1.2;color:#ddd">NMSA firearms instructor, NWDFA instructor &amp; training counsellor, news correspondent, and security expert</p>

  <div class="abs head" style="left:532px;top:133px;font-size:14.5px">Get In Touch</div>
  <div class="abs" style="left:532px;top:160px;width:18px;height:3px;background:var(--red)"></div>
  <div class="field" style="left:532px;top:181px">Name</div>
  <div class="field" style="left:798px;top:181px">Email</div>
  <div class="field" style="left:532px;top:235px">Phone</div>
  <div class="field" style="left:798px;top:235px">Message</div>
  <span class="btn">Submit &gt;</span>

  <nav class="footer-nav">
    <span>Home</span><span class="dot"></span>
    <span>Falconry Institute</span><span class="dot"></span>
    <span>Contact Us</span><span class="dot"></span>
    <span>Meet The Trainer</span>
  </nav>
  <div class="social"><span>Kestra</span><span>Chirpl</span><span>Snapwell</span></div>
  <div class="footer-rule"></div>
  <p class="copyright">Copyright Bright Harbor Guarding 2021 - All Rights Reserved</p>
</footer>

</body>
</html>
```